business cards

we want our logos on the back
the information on it are on the design I've uploaded
come up with whatever you think is best, we want something professional, sophisticated and sleek.

```html
<!DOCTYPE html>
<html lang="en">
<head>
<meta charset="utf-8">
<title>Meridian Health and Performance – Business Cards</title>
<link rel="stylesheet" href="https://fonts.googleapis.com/css2?family=Lato:wght@300;400;700;900&display=swap">
<style>
  :root {
    --bg: #1c1c1c;
    --card: #141414;
    --card-edge: #232323;
    --white: #f2f2f2;
    --grey: #b9b9b9;
    --green: #1fd11f;
  }
  * { margin: 0; padding: 0; box-sizing: border-box; }
  html, body { width: 1200px; height: 875px; overflow: hidden; }
  body {
    background: radial-gradient(ellipse at 40% 30%, #2b2b2b 0%, var(--bg) 70%);
    font-family: "Lato", Arial, sans-serif;
    color: var(--white);
    position: relative;
  }
  .card {
    position: absolute;
    top: 283px;
    width: 540px;
    height: 309px;
    background: var(--card);
    border: 1px solid var(--card-edge);
    border-radius: 18px;
    box-shadow: 0 24px 50px rgba(0,0,0,.55);
    overflow: hidden;
  }
  .card--front { left: 40px; }
  .card--back { left: 620px; }

  /* Front */
  .front-brand {
    position: absolute;
    left: 0; right: 0; top: 100px;
    text-align: center;
  }
  .wordmark {
    font-weight: 300;
    color: var(--white);
    letter-spacing: .32em;
    line-height: 1;
  }
  .front-brand .wordmark { font-size: 48px; padding-left: .32em; }
  .front-brand .brand-sub {
    margin-top: 10px;
    font-size: 11px;
    letter-spacing: .55em;
    padding-left: .55em;
    color: var(--grey);
  }
  .services {
    position: absolute;
    left: 0; right: 0; top: 204px;
    text-align: center;
    font-size: 11.5px;
    font-weight: 400;
    letter-spacing: .09em;
    color: var(--green);
  }

  /* Back */
  .back-info {
    position: absolute;
    right: 34px; top: 28px;
    text-align: right;
  }
  .back-info .wordmark { font-size: 30px; margin-right: -.32em; }
  .back-info .brand-sub {
    margin-top: 6px;
    font-size: 7.5px;
    letter-spacing: .5em;
    margin-right: -.5em;
    color: var(--grey);
  }
  .person-name {
    margin-top: 14px;
    font-size: 22px;
    font-weight: 900;
    color: var(--green);
    letter-spacing: .01em;
  }
  .person-role {
    font-size: 12px;
    line-height: 1.35;
    color: var(--white);
    margin-top: 2px;
  }
  .person-creds {
    font-size: 8.5px;
    color: var(--grey);
    margin-top: 3px;
  }
  .contact-list {
    list-style: none;
    margin-top: 14px;
    font-size: 11px;
    line-height: 1.45;
  }
  .contact-list li {
    display: flex;
    justify-content: flex-end;
    align-items: flex-start;
    gap: 8px;
    margin-bottom: 4px;
  }
  .contact-icon {
    flex: none;
    width: 13px; height: 13px;
    border-radius: 3px;
    background: var(--green);
    display: flex; align-items: center; justify-content: center;
    margin-top: 2px;
  }
  .contact-icon svg { width: 9px; height: 9px; }
  .contact-web { color: var(--grey); font-size: 10.5px; }
</style>
</head>
<body>

<section class="card card--front" aria-label="Card front">
  <div class="front-brand">
    <div class="wordmark">MERIDIAN</div>
    <div class="brand-sub">HEALTH AND PERFORMANCE</div>
  </div>
  <p class="services">PHYSIO • S&amp;C • COACHING • PERSONAL TRAINING • REHAB • RECOVERY</p>
</section>

<section class="card card--back" aria-label="Card back">
  <div class="back-info">
    <div class="wordmark">MERIDIAN</div>
    <div class="brand-sub">HEALTH AND PERFORMANCE</div>

    <h1 class="person-name">DANIEL KORAVOS</h1>
    <p class="person-role">Director / Physiotherapist<br>Strength &amp; Conditioning Coach</p>
    <p class="person-creds">BHlthSc, MPhysioPrac, MExSc(S&amp;C), ASCA Level 2</p>

    <ul class="contact-list">
      <li>
        <span>17 Linden Rd<br>Riverton VIC 3099</span>
        <span class="contact-icon"><svg viewBox="0 0 10 10"><path d="M5 1a3 3 0 0 0-3 3c0 2.2 3 5 3 5s3-2.8 3-5a3 3 0 0 0-3-3zm0 4.2a1.2 1.2 0 1 1 0-2.4 1.2 1.2 0 0 1 0 2.4z" fill="#141414"/></svg></span>
      </li>
      <li>
        <span>03 9000 1482</span>
        <span class="contact-icon"><svg viewBox="0 0 10 10"><path d="M2.3 1.2l1.5 1.6-.8 1.1c.5 1 1.2 1.7 2.2 2.2l1.1-.8 1.6 1.5-.9 1.4C4.4 8 2 5.6 1.8 2.1z" fill="#141414"/></svg></span>
      </li>
      <li>
        <span>03 9000 7315</span>
        <span class="contact-icon"><svg viewBox="0 0 10 10"><rect x="2" y="1.5" width="6" height="3" fill="#141414"/><rect x="1" y="4.5" width="8" height="3.5" rx=".6" fill="#141414"/></svg></span>
      </li>
      <li>
        <span>dan@meridianhp.com.au</span>
        <span class="contact-icon"><svg viewBox="0 0 10 10"><rect x="1" y="2.2" width="8" height="5.6" rx=".6" fill="#141414"/><path d="M1.3 2.6L5 5.4l3.7-2.8" stroke="#1fd11f" stroke-width=".8" fill="none"/></svg></span>
      </li>
      <li>
        <span class="contact-web">meridianhp.com.au</span>
        <span class="contact-icon"><svg viewBox="0 0 10 10"><circle cx="5" cy="5" r="3.6" fill="none" stroke="#141414" stroke-width="1"/><path d="M1.4 5h7.2M5 1.4c-1.6 2-1.6 5.2 0 7.2M5 1.4c1.6 2 1.6 5.2 0 7.2" stroke="#141414" stroke-width=".8" fill="none"/></svg></span>
      </li>
    </ul>
  </div>
</section>

</body>
</html>
```